Mixed Martial Arts gym that is known for high quality athletes, students and training

We need a business card designed that is unique and stands out. Something that is not so dark and boring but looks 'energetic' to those that are given it. The customers that would receive this card would be looking to sign up for martial arts or fitness training and this card is used for corporate sponsorships and networking as well.

Corwin Ashby-Lowe
0455013872 or 0467190534
Level 1, 218 Wexcombe Drive. Brackenvale NSW 2871
corwin@thornlevyquarrantgroup.com.au
www.thornlevyquarrantgroup.com

Training

```html
<!DOCTYPE html>
<html lang="en">
<head>
<meta charset="utf-8">
<title>Thornlevy Quarrant Group – Business Card</title>
<link rel="stylesheet" href="https://fonts.googleapis.com/css2?family=Open+Sans:wght@400;600;700&display=swap">
<style>
  :root {
    --bg: #e9e9e9;
    --card: #ffffff;
    --ink: #2b2b2b;
    --orange: #f39a1e;
    --black: #111111;
    --rule: #bdbdbd;
  }
  * { margin: 0; padding: 0; box-sizing: border-box; }
  html, body {
    width: 1200px; height: 1090px; overflow: hidden;
    background: var(--bg);
    font-family: "Open Sans", Arial, sans-serif;
    color: var(--ink);
  }
  .card {
    position: absolute;
    background: var(--card);
    border: 1px solid #3a3a3a;
    overflow: hidden;
  }
  .card--front { left: 300px; top: 30px; width: 866px; height: 496px; }
  .card--back  { left: 21px; top: 560px; width: 821px; height: 495px; }

  .brand {
    position: absolute;
    display: flex; align-items: center; gap: 14px;
    color: var(--orange);
    font-weight: 700;
    line-height: 1.05;
  }
  .brand__mark { width: 22px; height: 22px; background: var(--orange); flex: none; }
  .brand__name { font-size: 40px; }
  .brand__name span { display: block; }
  .card--front .brand { left: 48px; top: 186px; }
  .card--back .brand { left: 50%; top: 156px; transform: translateX(-50%); }
  .card--back .brand__name { font-size: 46px; }

  .divider {
    position: absolute; left: 412px; top: 128px;
    width: 2px; height: 262px; background: var(--rule);
  }
  .contact { position: absolute; left: 433px; top: 112px; }
  .contact__name { font-size: 26px; font-weight: 700; margin-bottom: 20px; }
  .contact__line {
    display: flex; align-items: center; gap: 8px;
    font-size: 19px; line-height: 36px;
  }
  .contact__line svg { width: 15px; height: 15px; flex: none; }
  .contact__address { font-size: 19.5px; line-height: 34px; margin-top: 12px; }

  .band { position: absolute; left: 0; bottom: 0; width: 866px; height: 100px; }
  .band__url {
    position: absolute; right: 30px; bottom: 14px;
    color: #fff; font-size: 21px; letter-spacing: 0.3px;
  }

  .back-url {
    position: absolute; left: 0; right: 0; top: 395px;
    text-align: center; font-size: 27px; letter-spacing: 2.5px;
    color: var(--black);
  }
</style>
</head>
<body>

<section class="card card--front">
  <div class="brand">
    <div class="brand__mark"></div>
    <div class="brand__name"><span>Thornlevy</span><span>Quarrant</span></div>
  </div>

  <div class="divider"></div>

  <div class="contact">
    <div class="contact__name">Corwin Ashby-Lowe</div>
    <div class="contact__line">
      <svg viewBox="0 0 16 16"><path d="M4 1.5 L6.5 4.5 L5 6.5 C6 8.5 7.5 10 9.5 11 L11.5 9.5 L14.5 12 L12.5 14.5 C7 14 2 9 1.5 3.5 Z" fill="none" stroke="#f39a1e" stroke-width="1.6" stroke-linejoin="round"/></svg>
      0455013872
    </div>
    <div class="contact__line">
      <svg viewBox="0 0 16 16"><path d="M4 1.5 L6.5 4.5 L5 6.5 C6 8.5 7.5 10 9.5 11 L11.5 9.5 L14.5 12 L12.5 14.5 C7 14 2 9 1.5 3.5 Z" fill="none" stroke="#f39a1e" stroke-width="1.6" stroke-linejoin="round"/></svg>
      0467190534
    </div>
    <div class="contact__line">
      <svg viewBox="0 0 16 16"><rect x="1" y="4" width="14" height="10" rx="1" fill="#f39a1e"/><path d="M1.5 4.5 L8 10 L14.5 4.5" fill="none" stroke="#fff" stroke-width="1.4"/></svg>
      corwin@thornlevyquarrantgroup.com.au
    </div>
    <div class="contact__address">Level 1, 218 Wexcombe Drive<br>Brackenvale NSW 2871</div>
  </div>

  <svg class="band" viewBox="0 0 866 100" preserveAspectRatio="none">
    <path d="M0 72 L410 72 C445 72 450 39 490 39 L866 39 L866 100 L0 100 Z" fill="#f39a1e"/>
    <path d="M0 68 L410 68 C442 68 448 36 488 36" fill="none" stroke="#111111" stroke-width="6"/>
  </svg>
  <div class="band__url">www.thornlevyquarrantgroup.com</div>
</section>

<section class="card card--back">
  <div class="brand">
    <div class="brand__mark"></div>
    <div class="brand__name"><span>Thornlevy</span><span>Quarrant</span></div>
  </div>
  <div class="back-url">www.thornlevyquarrantgroup.com</div>
</section>

</body>
</html>
```